Pelmar Grove에서 세계시장을 겨냥한 신제품 프리미엄 코르닉 스마트 체중계 출시에 맞춰 사용자 편의 위주의 가독성있는 반응형 앱의 UI UX디자인을 공모합니다. 앱의 주요 타겟층은 세계 20-40대 여성분들입니다. 향후 다양한 언어로 출시 예정이니 직관적, 전문적, 심플함위주의 가시성있는 그래픽을 선호하며 유저중심의 UI UX를 추구합니다.

```html
<!DOCTYPE html>
<html lang="ko">
<head>
<meta charset="utf-8">
<title>체중 측정 화면</title>
<link rel="stylesheet" href="https://fonts.googleapis.com/css2?family=Noto+Sans+KR:wght@300;400;500;700&display=swap">
<style>
  :root {
    --page-bg: #dfe6ee;
    --screen-bg: #f2f2f5;
    --header-start: #f28b5e;
    --header-end: #f4505c;
    --white: #ffffff;
    --ink: #1f1f24;
    --ink-soft: #8a8a92;
    --coral: #f06656;
    --teal: #31c98f;
    --pink: #e8457a;
    --line: #e6e6ea;
  }
  * { box-sizing: border-box; margin: 0; padding: 0; }
  html, body { width: 1200px; height: 1200px; overflow: hidden; }
  body {
    background: var(--page-bg);
    font-family: "Noto Sans KR", sans-serif;
    color: var(--ink);
    position: relative;
  }
  .screen {
    position: absolute; left: 330px; top: 54px;
    width: 540px; height: 1092px;
    background: var(--screen-bg);
    border-radius: 44px;
    overflow: hidden;
  }
  .header {
    position: absolute; left: 0; top: 0; width: 540px; height: 600px;
    background: linear-gradient(140deg, var(--header-start), var(--header-end));
    border-radius: 0 0 60px 0;
  }
  .avatar {
    position: absolute; left: 28px; top: 64px; width: 68px; height: 68px;
    border-radius: 50%; background: linear-gradient(160deg, #9fb3a6, #3b4a3f);
    border: 4px solid rgba(255,255,255,.55);
  }
  .add-button {
    position: absolute; left: 459px; top: 60px; width: 44px; height: 44px;
    border-radius: 50%; background: rgba(255,255,255,.28);
  }
  .ring {
    position: absolute; left: 85px; top: 116px; width: 360px; height: 360px;
    border-radius: 50%; border: 2px solid rgba(255,255,255,.55);
  }
  .user-name {
    position: absolute; left: 0; width: 530px; top: 208px; text-align: center;
    color: var(--white); font-size: 38px; font-weight: 300;
  }
  .weight {
    position: absolute; left: 0; width: 530px; top: 262px; text-align: center;
    color: var(--white); font-weight: 500; font-size: 80px; line-height: 1;
  }
  .weight small { font-size: 48px; }
  .weight .unit { font-size: 40px; margin-left: 4px; }
  .measured-at {
    position: absolute; left: 0; width: 530px; top: 355px; text-align: center;
    color: rgba(255,255,255,.85); font-size: 17px;
  }
  .goal-badge {
    position: absolute; left: 352px; top: 370px; width: 114px; height: 114px;
    border-radius: 50%; background: var(--white);
    box-shadow: 0 0 0 9px rgba(255,255,255,.35), 0 8px 18px rgba(200,50,60,.3);
    text-align: center; padding-top: 26px;
  }
  .goal-badge span { display: block; color: var(--coral); font-size: 16px; font-weight: 500; margin-top: 2px; }
  .stats-card {
    position: absolute; left: 33px; top: 520px; width: 476px; height: 148px;
    background: var(--white); border-radius: 74px;
    box-shadow: 0 8px 24px rgba(0,0,0,.06);
  }
  .stats { display: flex; padding-top: 24px; }
  .stat { flex: 1; text-align: center; }
  .stat + .stat { border-left: 1px solid var(--line); }
  .stat-label { color: var(--coral); font-size: 17px; }
  .stat-value { font-size: 30px; font-weight: 700; margin-top: 6px; }
  .stat-value small { font-size: 20px; font-weight: 500; }
  .compare-date { text-align: center; color: var(--ink-soft); font-size: 15px; margin-top: 10px; }
  .metric {
    position: absolute; left: 21px; width: 485px; height: 111px;
    background: var(--white); border-radius: 14px; padding: 22px 24px;
  }
  .metric-name { font-size: 17px; font-weight: 500; }
  .metric-value { font-size: 32px; font-weight: 700; color: var(--teal); margin-top: 2px; }
  .metric-value small { font-size: 20px; font-weight: 400; }
  .metric-value.pink { color: var(--pink); }
  .chevron { position: absolute; right: 26px; top: 46px; }
  .tab-bar {
    position: absolute; left: 0; top: 1020px; width: 540px; height: 72px;
    background: var(--white); display: flex; border-top: 1px solid var(--line);
  }
  .tab { flex: 1; text-align: center; padding-top: 12px; font-size: 13px; color: var(--ink-soft); }
  .tab svg { display: block; margin: 0 auto 4px; }
  .tab.active { color: var(--coral); }
</style>
</head>
<body>
<main class="screen">
  <section class="header">
    <div class="avatar" role="img" aria-label="사용자 프로필 사진"></div>
    <svg class="add-button" viewBox="0 0 44 44"><path d="M22 14v16M14 22h16" stroke="#fff" stroke-width="2.4" stroke-linecap="round"/></svg>
    <div class="ring"></div>
    <p class="user-name">박서윤</p>
    <p class="weight">86<small>.75</small><span class="unit">kg</span></p>
    <p class="measured-at">2019. 7. 9 오후 4:11</p>
    <div class="goal-badge">
      <svg width="36" height="34" viewBox="0 0 36 34"><path d="M18 3l4.6 9.4 10.4 1.5-7.5 7.3 1.8 10.3L18 26.6l-9.3 4.9 1.8-10.3L3 13.9l10.4-1.5z" fill="#f7a23c"/><circle cx="30" cy="5" r="3" fill="#f06656"/></svg>
      <span>설정목표</span>
    </div>
  </section>

  <section class="stats-card">
    <div class="stats">
      <div class="stat"><p class="stat-label">체중</p><p class="stat-value">+8.75<small>kg</small></p></div>
      <div class="stat"><p class="stat-label">체지방률</p><p class="stat-value">+5.4<small>%</small></p></div>
      <div class="stat"><p class="stat-label">BMI</p><p class="stat-value">0.0</p></div>
    </div>
    <p class="compare-date">비교 대상 2019. 7. 9 오후 4:11</p>
  </section>

  <article class="metric" style="top:699px">
    <p class="metric-name">심박율</p>
    <p class="metric-value">73.0<small> bpm</small></p>
    <svg class="chevron" width="20" height="12" viewBox="0 0 20 12"><path d="M2 2l8 8 8-8" fill="none" stroke="#333" stroke-width="2"/></svg>
  </article>
  <article class="metric" style="top:827px">
    <p class="metric-name">심장지수</p>
    <p class="metric-value">2.6<small> L/Min/M</small></p>
    <svg class="chevron" width="20" height="12" viewBox="0 0 20 12"><path d="M2 2l8 8 8-8" fill="none" stroke="#333" stroke-width="2"/></svg>
  </article>
  <article class="metric" style="top:955px">
    <p class="metric-name">체중</p>
    <p class="metric-value pink">86.75<small>kg</small></p>
    <svg class="chevron" width="20" height="12" viewBox="0 0 20 12"><path d="M2 10l8-8 8 8" fill="none" stroke="#333" stroke-width="2"/></svg>
  </article>

  <nav class="tab-bar">
    <div class="tab active">
      <svg width="30" height="30" viewBox="0 0 30 30"><rect x="5" y="5" width="19" height="21" rx="2" fill="none" stroke="#f06656" stroke-width="2"/><path d="M10 13h9M10 18h6" stroke="#f06656" stroke-width="2"/><path d="M20 4l6 6" stroke="#f06656" stroke-width="2"/></svg>측정
    </div>
    <div class="tab">
      <svg width="30" height="30" viewBox="0 0 30 30"><rect x="5" y="16" width="4" height="9" fill="none" stroke="#8a8a92" stroke-width="1.8"/><rect x="13" y="11" width="4" height="14" fill="none" stroke="#8a8a92" stroke-width="1.8"/><rect x="21" y="6" width="4" height="19" fill="none" stroke="#8a8a92" stroke-width="1.8"/></svg>비교
    </div>
    <div class="tab">
      <svg width="30" height="30" viewBox="0 0 30 30"><circle cx="15" cy="10" r="5" fill="none" stroke="#8a8a92" stroke-width="1.8"/><path d="M5 26c1-6 5-9 10-9s9 3 10 9" fill="none" stroke="#8a8a92" stroke-width="1.8"/></svg>나
    </div>
  </nav>
</main>
</body>
</html>
```